Book Cover E-Book & Print, TVL & QN

Last Update 13/11: I just noticed that Pixel Guild stripped out the URL of the Chatterly page from my original posting, but if you go to Chatterly and do a search for Traditional Archery groups, it will come up. That should give an idea. I have also attached a screen shot as an update to the project.

UPDATE 8/11: PLEASE NOTE THE FOLLOWING, THIS QN CRITICAL:

>>>
1) the figure should be male ('Harold Penfield'), apologies for inducing confusion originally by talking about a female archer. The novel is also Dystopian Fantasy, so the clothes need to be non-descript modern, not hooded, Elven or whatever as in classical fantasy stories. There is actually very little magic in Harold Penfield's Hollow.

2) the bow needs to be positioned around the upper outer edge of the moon, as described in the specs: "In this, the archer draws their bow aimed into the night sky against a near-full moon, attempting to align the bow itself with one upper edge of the moon". There is more text in the specs below that should help give you an idea of what I want here, otherwise ask for clarification.

3) please have the archer pointing the bow to the right and upwards, kind of like the 2 o'clock position on the moon.

4) please draw a primitive bow, just a semi-circle as though it's rough-hewn from a tree limb (which it is in the book). No recurves, fancy knobs or spaces etc.
>>

..........

Everyone needs a second chance...

While searching for his missing wife, Harold Penfield falls through a portal between earth and the strange land of Quessovar. With the ability to now travel between the two worlds almost at will, he tracks his wife along a trail of clues she leaves in her own mysterious odyssey. But the trail grows faint, and each trip Harold makes reveals foreboding changes taking place in both worlds.

The dangers soar on one journey as an entity latches on to him, an evil bent on plundering Harold's old world to remake Quessovar in its own image.

With the two worlds disintegrating, the portal fracturing and his nemesis close behind, Harold must choose---leave the fight against evil to others and rebuild whatever life he can or make a final effort to be reunited with his love.

>>
Then she stepped back onto the high rock and held the bow out from her. “It’s part of a spell, the most powerful magic we Tulk know. But only part of it, you understand. When something is desired with the whole soul but seems out of reach, it is like the moon that hasn't yet formed to fullness or has passed the high point of its glory. By doing this, we draw her silver skin from one side of the circle to the other. Watch.”

Drawing the string back beyond her ear she pushed the bow out in front with the other hand, as though testing the extent of the weapon's draw. Then she raised it above her head, holding its curve along one edge of the moon's glare. As Penfield manoeuvred to get a better view the monstrous effort of holding the powerful bow at full draw began to tell on Merusha. Her musculature bulged and knotted from wrist to wrist, shaking and sheening sweat where it pinched at the base of the neck.

“Do you see?” she pleaded, her body quaking.

And suddenly, yes, he could see it. As he moved a little closer to her and bobbed from side to side it came into view like focusing binoculars, blurring back and forth until the image clarified and settled.

The arc of the bow melted onto one edge of the silver backdrop, and where she’d drawn the string beyond the normal anchor point on her head, its pinched 'V' met the opposite curve of the near-full moon, almost exactly.

“Yes,” he said.
>>

>>

>>

Colors

Requirements
Must have
• UPDATE 8/11: PLEASE NOTE THE FOLLOWING, THIS QN CRITICAL:
• >>>
• 1) the figure should be male ('Harold Penfield'), apologies for inducing confusion originally by talking about a female archer. The novel is also Dystopian Fantasy, so the clothes need to be non-descript modern, not hooded, Elven or whatever as in classical fantasy stories. There is actually very little magic in Harold Penfield's Hollow.
• 2) the bow needs to be positioned around the upper outer edge of the moon, as described in the specs: "In this, the archer draws their bow aimed into the night sky against a near-full moon, attempting to align the bow itself with one upper edge of the moon". There is more text in the specs below that should help give you an idea of what I want here, otherwise ask for clarification.
• 3) please have the archer pointing the bow to the right and upwards, kind of like the 2 o'clock position on the moon.
• 4) please draw a primitive bow, just a semi-circle as though it's rough-hewn from a tree limb (which it is in the book). No recurves, fancy knobs or spaces etc.
• >>

```html
<!DOCTYPE html>
<html lang="en">
<head>
<meta charset="utf-8">
<title>Harold Penfield's Hollow — Back Cover</title>
<link rel="stylesheet" href="https://fonts.googleapis.com/css2?family=Gelasio:ital,wght@0,400;0,700;1,400&display=swap">
<style>
  :root {
    --sky-top: #0d1431;
    --sky-mid: #2c2c66;
    --sky-low: #4b4283;
    --sky-horizon: #6e78bd;
    --ink: #f4f2f7;
  }
  * { margin: 0; padding: 0; box-sizing: border-box; }
  html, body { width: 770px; height: 1200px; overflow: hidden; background: var(--sky-top); }
  .back-cover {
    position: relative;
    width: 770px;
    height: 1200px;
    overflow: hidden;
    font-family: "Gelasio", Georgia, serif;
    color: var(--ink);
  }
  .night-sky-photo {
    position: absolute;
    inset: 0;
    background: linear-gradient(180deg, var(--sky-top) 0%, var(--sky-mid) 50%, var(--sky-low) 78%, var(--sky-horizon) 100%);
  }
  .title {
    position: absolute;
    top: 42px;
    left: 62px;
    width: 680px;
    font-weight: 700;
    font-size: 36px;
    line-height: 1.2;
    white-space: nowrap;
  }
  .blurb, .review, .bio {
    position: absolute;
    left: 65px;
    font-size: 26px;
    line-height: 30.4px;
    text-shadow: 0 1px 2px rgba(0,0,0,0.35);
  }
  .blurb { width: 672px; }
  .blurb-one { top: 96px; }
  .blurb-two { top: 340px; }
  .blurb-three { top: 462px; }
  .review { top: 604px; width: 700px; line-height: 32px; white-space: nowrap; }
  .review-quote { font-style: italic; }
  .bio { top: 826px; width: 660px; font-size: 25px; }
</style>
</head>
<body>
<main class="back-cover">
  <div class="night-sky-photo" role="img" aria-label="Photograph of a starry night sky with the Milky Way above a dusky horizon and a grassy hillside"></div>

  <h1 class="title">Everyone Needs A Second Chance...</h1>

  <p class="blurb blurb-one">While searching for his missing wife, Harold Penfield falls through a portal between earth and the strange land of Quessovar. With the ability to now travel between the two worlds almost at will, he tracks his wife along a trail of clues she leaves in her own mysterious odyssey. But the trail grows faint, and each trip Harold makes reveals foreboding changes taking place in both worlds.</p>

  <p class="blurb blurb-two">The dangers soar on one journey as an entity latches on to him, an evil bent on plundering Harold's old world to remake Quessovar in its own image.</p>

  <p class="blurb blurb-three">With the two worlds disintegrating, the portal fracturing and his nemesis close behind, Harold must choose — leave the fight against evil to others and rebuild whatever life he can or make a final effort to be reunited with his love.</p>

  <p class="review"><span class="review-quote">“A powerful, engrossing tale of a man who seeks his<br>love, and finds his destiny in a world beyond worlds.<br>Harold Penfield’s Hollow is deceptively, elegantly and<br>hauntingly written, a tale that echoes quietly<br>in the mind after the end, like a favourite<br>song.”</span> — Dale Whitcombe, author of the Ember Cycle</p>

  <p class="bio">Corin Vale grew up in country Australia and moved to Melbourne in his twenties where he now lives with his wife. When he's not writing you will likely find him reading just about anything from poetry and genre fiction to non-fiction, especially primitive and traditional archery books.</p>
</main>
</body>
</html>
```